Design a Brochure

Hi, I'd like some graphic design for a healthcare programme called Wide Open Sky. I need a logo (that isn't just words) and an A4 brochure to introduce the benefits of the programme. I also need 5 icons for each of the 5 stages of the programme which are Focus, Formulate, Feel, Frame and Flow. It's a wellness programme for mind and body health so I'm looking for inspiring designs which reflect this. I don't want it to look like a brochure for a gym. I'd prefer images of people looking happy and healthy, not treadmills and weights. I hope you lovely creative people can really help me bring this project to life. I've attached the brochure copy for the inside left, inside right and back cover.

```html
<!DOCTYPE html>
<html lang="en">
<head>
<meta charset="utf-8">
<title>Wide Open Sky – Brochure</title>
<link rel="stylesheet" href="https://fonts.googleapis.com/css2?family=Montserrat:wght@400;500;600;700&family=Open+Sans:ital,wght@0,400;0,600;1,400&display=swap">
<style>
:root{
  --backdrop:#3f7712;
  --green:#7cbb2c;
  --green-deep:#5d9a19;
  --green-pale:#eef6e2;
  --orange:#f2931f;
  --ink:#4a4a4a;
  --white:#ffffff;
  --sky:#cfe3f2;
  --grass:#6fa43a;
}
*{box-sizing:border-box;margin:0;padding:0}
html,body{width:1200px;height:4047px;overflow:hidden}
body{background:var(--backdrop);font-family:"Open Sans",Arial,sans-serif;color:var(--ink);position:relative}

.page{position:absolute;width:490px;height:647px;overflow:hidden;background:var(--white)}
.solo-cover{left:355px;top:70px;box-shadow:0 20px 40px rgba(0,0,0,.25)}
.spread{position:absolute;left:110px;width:980px;height:647px;box-shadow:0 20px 40px rgba(0,0,0,.25)}
.spread .page.left{left:0;top:0}
.spread .page.right{left:490px;top:0}
.row-2{top:880px}
.row-3{top:1700px}
.row-4{top:2525px}
.row-5{top:3270px}

/* front cover */
.cover-photo{position:absolute;inset:0;background:linear-gradient(180deg,#ffffff 0%,#f4f8fb 22%,var(--sky) 45%,#b9d4a4 62%,var(--grass) 78%,#4f8a25 100%)}
.brand{position:absolute;left:34px;top:42px;display:flex;align-items:center;gap:10px}
.brand-dot{width:28px;height:28px;border-radius:50%;background:var(--orange)}
.brand-name{font-family:"Montserrat",Arial,sans-serif;font-weight:600;font-size:17px;color:var(--green-deep)}
.cover-tagline{position:absolute;left:34px;top:140px;width:270px;font-family:"Montserrat",Arial,sans-serif;font-weight:600;font-size:10.5px;line-height:14px;color:var(--orange)}
.cover-title{position:absolute;left:34px;top:198px;width:300px;font-family:"Montserrat",Arial,sans-serif;font-weight:700;font-size:21px;line-height:26px;color:var(--green)}
.cover-sub{position:absolute;left:34px;top:262px;width:250px;font-size:10px;line-height:14px;color:var(--ink)}
.swoosh{position:absolute;left:0;bottom:0;width:490px;height:80px}

/* back cover */
.back{background:linear-gradient(160deg,#8fc63e 0%,var(--green) 45%,#6aa823 100%)}
.back-title{position:absolute;left:46px;top:252px;font-family:"Montserrat",Arial,sans-serif;font-size:12px;color:var(--white)}
.back-title strong{font-weight:700}
.quotes{position:absolute;left:46px;top:278px;width:414px;display:flex;flex-direction:column;gap:8px}
.quote{border:1.2px solid rgba(255,255,255,.85);border-radius:6px;padding:6px 10px 4px;color:var(--white);font-size:8.4px;line-height:12.5px}
.quote cite{display:block;text-align:right;font-style:normal;font-weight:600;font-size:8.4px;margin-top:3px;padding-top:2px;border-top:1px solid rgba(255,255,255,.7)}

/* inside left */
.about-band{position:absolute;left:0;top:0;width:490px;height:192px;background:linear-gradient(180deg,#a3d05c 0%,var(--green) 60%,#86c036 100%)}
.about-band-photo{position:absolute;right:0;top:0;width:260px;height:90px;background:linear-gradient(90deg,rgba(255,255,255,0),rgba(232,240,220,.5))}
.about-title{position:absolute;left:39px;top:64px;font-family:"Montserrat",Arial,sans-serif;font-size:15px;color:var(--white)}
.about-title strong{font-weight:700}
.about-copy{position:absolute;left:39px;top:88px;width:415px;font-size:8.3px;line-height:12.5px;color:var(--white)}
.plan-title{position:absolute;left:39px;top:204px;font-family:"Montserrat",Arial,sans-serif;font-size:14px;color:var(--orange)}
.plan-title strong{font-weight:700}
.step{position:absolute}
.step-icon{float:left;width:26px;height:26px;margin:2px 8px 2px 0}
.step-name{font-family:"Montserrat",Arial,sans-serif;font-weight:700;font-size:9.5px;line-height:13px;color:var(--orange)}
.step-copy{font-size:8.2px;line-height:12px;text-align:justify}
.step.col-a{left:39px;width:240px}
.step.col-b{left:300px;width:180px}
.man-photo{position:absolute;left:290px;top:450px;width:200px;height:197px;background:linear-gradient(180deg,#eef3f6 0%,#c9d8e3 40%,#8fa9bf 70%,#d9cfba 100%)}

/* inside right */
.woman-photo{position:absolute;left:27px;top:50px;width:170px;height:204px;background:linear-gradient(180deg,#f7f8f9 0%,#dfe4ea 50%,#a7b4c6 80%,#d9479a 92%,#ffffff 100%)}
.intro{position:absolute;left:222px;top:12px;width:245px;font-size:8.3px;line-height:12px}
.included{position:absolute;left:222px;top:64px;width:245px;height:206px;background:var(--green-pale);border-radius:5px;padding:8px 10px}
.included h3{font-family:"Montserrat",Arial,sans-serif;font-weight:700;font-size:11.5px;color:var(--orange);margin-bottom:4px}
.included ul{list-style:none}
.included li{font-size:8px;line-height:20px;font-style:italic;white-space:nowrap}
.included li::before{content:"•";color:var(--green);margin-right:5px;font-style:normal}
.after-title{position:absolute;left:0;top:283px;width:490px;text-align:center;font-family:"Montserrat",Arial,sans-serif;font-weight:600;font-size:11px;color:var(--green)}
.outcomes{position:absolute;left:27px;top:305px;width:440px;display:grid;grid-template-columns:repeat(3,1fr);gap:7px 10px}
.outcome{border:1.2px solid var(--green);border-radius:12px;height:27px;display:flex;align-items:center;justify-content:center;text-align:center;font-size:7.6px;line-height:9.5px;padding:0 6px}
.price-title{position:absolute;left:0;top:394px;width:490px;text-align:center;font-family:"Montserrat",Arial,sans-serif;font-weight:700;font-size:11px;color:var(--green)}
.price-title span{color:var(--orange)}
.price-note{position:absolute;left:0;top:411px;width:490px;text-align:center;font-size:7.6px}
.prices{position:absolute;left:0;top:428px;width:490px;display:flex;justify-content:center;gap:12px}
.price{background:var(--green);color:var(--white);border-radius:6px;width:112px;padding:2px 0;text-align:center}
.price b{display:block;font-family:"Montserrat",Arial,sans-serif;font-size:14px;line-height:17px}
.price i{display:block;font-size:7px;line-height:10px;color:#fde3bd}
.family-photo{position:absolute;left:0;top:477px;width:490px;height:170px;background:linear-gradient(180deg,#bcd88a 0%,#8cbf4e 45%,var(--grass) 100%)}
</style>
</head>
<body>

<section class="page solo-cover" aria-label="Front cover">
  <div class="cover-photo" role="img" aria-label="Photo of a woman in a white dress with arms open in a sunny green meadow"></div>
  <div class="brand"><span class="brand-dot"></span><span class="brand-name">Wide Open Sky</span></div>
  <p class="cover-tagline">Follow our five step plan and in three months you'll experience life as you've never done before.</p>
  <h1 class="cover-title">Experience life as you've never done before.</h1>
  <p class="cover-sub">An unique and exciting programme designed to help you take control of your health and your life.</p>
  <svg class="swoosh" viewBox="0 0 490 110" preserveAspectRatio="none"><path d="M0 70 C150 40 330 30 490 20 L490 110 L0 110Z" fill="#ffffff"/><path d="M0 84 C160 60 330 44 490 36 L490 110 L0 110Z" fill="#f2931f"/><path d="M0 90 C160 70 330 56 490 50 L490 110 L0 110Z" fill="#7cbb2c"/></svg>
</section>

<section class="spread row-2" aria-label="Back and front cover">
  <div class="page left back">
    <h2 class="back-title">What people are saying about <strong>Wide Open Sky</strong></h2>
    <div class="quotes">
      <blockquote class="quote">Wide Open Sky has changed my life. It's so much more than pain relief, it's a total mind and body re-set. If you want to get to the bottom of what's stopping you being healthy and really make changes this is for you.<cite>Marcus</cite></blockquote>
      <blockquote class="quote">I've tried so many things to improve my health over the years but the Wide Open Sky programme was exactly what I needed. Now I really feel like I've got my life back.<cite>Tom</cite></blockquote>
      <blockquote class="quote">Everyone should do this! The results are incredible. I thought I was just going to learn how to relax and improve my back pain but this changes everything. I'm thinking clearer, I'm more energetic, I'm more motivated and I feel like I can achieve anything.<cite>Clara</cite></blockquote>
      <blockquote class="quote">Wide Open Sky has made me more confident, more in control and more healthy. I really am unbreakable now! Thank you<cite>Jen</cite></blockquote>
      <blockquote class="quote">I was worried I wouldn't be able to manage all the five steps but it was so easy. You're supported all along the way and everything makes so much sense. I feel amazing now.<cite>Nina</cite></blockquote>
    </div>
  </div>
  <div class="page right">
    <div class="cover-photo" role="img" aria-label="Photo of a woman in a white dress with arms open in a sunny green meadow"></div>
    <div class="brand"><span class="brand-dot"></span><span class="brand-name">Wide Open Sky</span></div>
    <p class="cover-tagline">Follow our five step plan and in three months you'll experience life as you've never done before.</p>
    <h2 class="cover-title">Experience life as you've never done before.</h2>
    <p class="cover-sub">An unique and exciting programme designed to help you take control of your health and your life.</p>
    <svg class="swoosh" viewBox="0 0 490 110" preserveAspectRatio="none"><path d="M0 70 C150 40 330 30 490 20 L490 110 L0 110Z" fill="#ffffff"/><path d="M0 84 C160 60 330 44 490 36 L490 110 L0 110Z" fill="#f2931f"/><path d="M0 90 C160 70 330 56 490 50 L490 110 L0 110Z" fill="#7cbb2c"/></svg>
  </div>
</section>

<section class="spread row-3" aria-label="Inside spread">
  <div class="page left">
    <div class="about-band"><div class="about-band-photo" role="img" aria-label="Faded photo of a woman stretching outdoors"></div></div>
    <h2 class="about-title">About the <strong>Program</strong></h2>
    <p class="about-copy">Welcome to our unique and exciting programme designed to help you take control of your health and your life. When you join Wide Open Sky your mind and body are connected and you become unbreakable. You'll enjoy more happiness and will take on life's challenges with ease. Most health programmes look to address physical or emotional problems alone. But you can't have one without the other! Follow our five step plan and in three months you'll experience life as you've never done before.</p>
    <h3 class="plan-title">Five Step <strong>Plan</strong></h3>
    <div class="step col-a" style="top:230px">
      <svg class="step-icon" viewBox="0 0 34 34"><circle cx="17" cy="17" r="17" fill="#7cbb2c"/><circle cx="17" cy="17" r="9" fill="none" stroke="#fff" stroke-width="2"/><circle cx="17" cy="17" r="3.5" fill="#fff"/></svg>
      <div class="step-name">Focus</div>
      <p class="step-copy">Focus your intention. Complete our simple online questionnaire to determine your level of commitment and get clear on exactly what you need to change. Focus is your key to success!</p>
    </div>
    <div class="step col-a" style="top:312px">
      <svg class="step-icon" viewBox="0 0 34 34"><circle cx="17" cy="17" r="17" fill="#7cbb2c"/><path d="M11 23 L21 11 L24 14 L14 26 L10 27Z" fill="none" stroke="#fff" stroke-width="2" stroke-linejoin="round"/></svg>
      <div class="step-name">Formulate</div>
      <p class="step-copy">Formulate your new future. Enter our Formulation Suite where you'll receive expert instructions and a new guided meditation each month. Follow this up daily in the comfort of your own home and use your mind to re-programme your body for health and happiness.</p>
    </div>
    <div class="step col-a" style="top:410px">
      <svg class="step-icon" viewBox="0 0 34 34"><circle cx="17" cy="17" r="17" fill="#7cbb2c"/><path d="M17 25 C9 19 8 15 10 12 C12 9.5 15.5 10 17 13 C18.5 10 22 9.5 24 12 C26 15 25 19 17 25Z" fill="none" stroke="#fff" stroke-width="2" stroke-linejoin="round"/></svg>
      <div class="step-name">Feel</div>
      <p class="step-copy">Feel in control. In the Wide Open Sky Journal we'll guide you in ways to re-frame your limiting beliefs and practice gratitude. This powerful daily ritual will stop anything holding you back and build confidence and self-esteem in abundance.</p>
    </div>
    <div class="step col-a" style="top:510px">
      <svg class="step-icon" viewBox="0 0 34 34"><circle cx="17" cy="17" r="17" fill="#7cbb2c"/><circle cx="17" cy="10" r="3" fill="#fff"/><path d="M17 14 L17 21 M10 16 L24 16 M17 21 L12 27 M17 21 L22 27" stroke="#fff" stroke-width="2" stroke-linecap="round"/></svg>
      <div class="step-name">Frame</div>
      <p class="step-copy">Change your frame. Posture is an outer reflection of your inner health. Pain, fatigue and many common health conditions result from poor posture. Spinal adjustments twice a week will realign your frame, getting you back into shape and supercharging your body's innate healing power.</p>
    </div>
    <div class="step col-b" style="top:230px">
      <svg class="step-icon" viewBox="0 0 34 34"><circle cx="17" cy="17" r="17" fill="#7cbb2c"/><circle cx="19" cy="9" r="2.8" fill="#fff"/><path d="M18 13 L15 20 L19 23 L18 28 M15 20 L11 26 M17 15 L22 18 M16 15 L12 17" stroke="#fff" stroke-width="2" stroke-linecap="round" fill="none"/></svg>
      <div class="step-name">Flow</div>
      <p class="step-copy">Flow is movement. Commit to walking for half an hour daily to get your body in flow. We've made it simple to track using our Flow App. Then what's your next move? What happens when you complete this programme and truly join Wide Open Sky? Take our Find Your Flow Survey and see if you're ready to join our Unbreakable Community.</p>
    </div>
    <div class="man-photo" role="img" aria-label="Photo of a man meditating cross-legged on a beach"></div>
  </div>

  <div class="page right">
    <div class="woman-photo" role="img" aria-label="Photo of a woman meditating on a pink yoga mat"></div>
    <p class="intro">One step on its own from this programme will make a difference, but follow all five and you really will join Wide Open Sky and become Unbreakable.</p>
    <div class="included">
      <h3>What's included?</h3>
      <ul>
        <li>Focus Questionnaire access</li>
        <li>Formulation Suite Sessions x 3</li>
        <li>Guided Meditation Downloads x 3</li>
        <li>Wide Open Sky Journal</li>
        <li>Adjustment Sessions x 2 per week</li>
        <li>Flow App access</li>
        <li>Find Your Flow Survey</li>
        <li>Invitation to join our Unbreakable Community</li>
      </ul>
    </div>
    <h3 class="after-title">After This Programme You Will:</h3>
    <div class="outcomes">
      <div class="outcome">Experience clear thinking</div>
      <div class="outcome">Master your physical and emotional health</div>
      <div class="outcome">Conquer your limiting beliefs</div>
      <div class="outcome">Improve confidence, self esteem and resilience</div>
      <div class="outcome">Enjoy amazing posture</div>
      <div class="outcome">Become Unbreakable</div>
    </div>
    <h3 class="price-title">How much would <span>all this mean to you?</span></h3>
    <p class="price-note">One amazing programme, two easy options</p>
    <div class="prices">
      <div class="price"><b>£1297</b><i>one off fee</i></div>
      <div class="price"><b>£452</b><i>x3 monthly instalments</i></div>
    </div>
    <div class="family-photo" role="img" aria-label="Photo of a happy family lying together on green grass"></div>
  </div>
</section>

<section class="spread row-4" aria-label="Back and front cover, flat">
  <div class="page left back">
    <h2 class="back-title">What people are saying about <strong>Wide Open Sky</strong></h2>
    <div class="quotes">
      <blockquote class="quote">Wide Open Sky has changed my life. It's so much more than pain relief, it's a total mind and body re-set. If you want to get to the bottom of what's stopping you being healthy and really make changes this is for you.<cite>Marcus</cite></blockquote>
      <blockquote class="quote">I've tried so many things to improve my health over the years but the Wide Open Sky programme was exactly what I needed. Now I really feel like I've got my life back.<cite>Tom</cite></blockquote>
      <blockquote class="quote">Everyone should do this! The results are incredible. I thought I was just going to learn how to relax and improve my back pain but this changes everything. I'm thinking clearer, I'm more energetic, I'm more motivated and I feel like I can achieve anything.<cite>Clara</cite></blockquote>
      <blockquote class="quote">Wide Open Sky has made me more confident, more in control and more healthy. I really am unbreakable now! Thank you<cite>Jen</cite></blockquote>
      <blockquote class="quote">I was worried I wouldn't be able to manage all the five steps but it was so easy. You're supported all along the way and everything makes so much sense. I feel amazing now.<cite>Nina</cite></blockquote>
    </div>
  </div>
  <div class="page right">
    <div class="cover-photo" role="img" aria-label="Photo of a woman in a white dress with arms open in a sunny green meadow"></div>
    <div class="brand"><span class="brand-dot"></span><span class="brand-name">Wide Open Sky</span></div>
    <p class="cover-tagline">Follow our five step plan and in three months you'll experience life as you've never done before.</p>
    <h2 class="cover-title">Experience life as you've never done before.</h2>
    <p class="cover-sub">An unique and exciting programme designed to help you take control of your health and your life.</p>
    <svg class="swoosh" viewBox="0 0 490 110" preserveAspectRatio="none"><path d="M0 70 C150 40 330 30 490 20 L490 110 L0 110Z" fill="#ffffff"/><path d="M0 84 C160 60 330 44 490 36 L490 110 L0 110Z" fill="#f2931f"/><path d="M0 90 C160 70 330 56 490 50 L490 110 L0 110Z" fill="#7cbb2c"/></svg>
  </div>
</section>

<section class="spread row-5" aria-label="Inside spread, flat">
  <div class="page left">
    <div class="about-band"><div class="about-band-photo" role="img" aria-label="Faded photo of a woman stretching outdoors"></div></div>
    <h2 class="about-title">About the <strong>Program</strong></h2>
    <p class="about-copy">Welcome to our unique and exciting programme designed to help you take control of your health and your life. When you join Wide Open Sky your mind and body are connected and you become unbreakable. You'll enjoy more happiness and will take on life's challenges with ease. Most health programmes look to address physical or emotional problems alone. But you can't have one without the other! Follow our five step plan and in three months you'll experience life as you've never done before.</p>
    <h3 class="plan-title">Five Step <strong>Plan</strong></h3>
    <div class="step col-a" style="top:230px">
      <svg class="step-icon" viewBox="0 0 34 34"><circle cx="17" cy="17" r="17" fill="#7cbb2c"/><circle cx="17" cy="17" r="9" fill="none" stroke="#fff" stroke-width="2"/><circle cx="17" cy="17" r="3.5" fill="#fff"/></svg>
      <div class="step-name">Focus</div>
      <p class="step-copy">Focus your intention. Complete our simple online questionnaire to determine your level of commitment and get clear on exactly what you need to change. Focus is your key to success!</p>
    </div>
    <div class="step col-a" style="top:312px">
      <svg class="step-icon" viewBox="0 0 34 34"><circle cx="17" cy="17" r="17" fill="#7cbb2c"/><path d="M11 23 L21 11 L24 14 L14 26 L10 27Z" fill="none" stroke="#fff" stroke-width="2" stroke-linejoin="round"/></svg>
      <div class="step-name">Formulate</div>
      <p class="step-copy">Formulate your new future. Enter our Formulation Suite where you'll receive expert instructions and a new guided meditation each month. Follow this up daily in the comfort of your own home and use your mind to re-programme your body for health and happiness.</p>
    </div>
    <div class="step col-a" style="top:410px">
      <svg class="step-icon" viewBox="0 0 34 34"><circle cx="17" cy="17" r="17" fill="#7cbb2c"/><path d="M17 25 C9 19 8 15 10 12 C12 9.5 15.5 10 17 13 C18.5 10 22 9.5 24 12 C26 15 25 19 17 25Z" fill="none" stroke="#fff" stroke-width="2" stroke-linejoin="round"/></svg>
      <div class="step-name">Feel</div>
      <p class="step-copy">Feel in control. In the Wide Open Sky Journal we'll guide you in ways to re-frame your limiting beliefs and practice gratitude. This powerful daily ritual will stop anything holding you back and build confidence and self-esteem in abundance.</p>
    </div>
    <div class="step col-a" style="top:510px">
      <svg class="step-icon" viewBox="0 0 34 34"><circle cx="17" cy="17" r="17" fill="#7cbb2c"/><circle cx="17" cy="10" r="3" fill="#fff"/><path d="M17 14 L17 21 M10 16 L24 16 M17 21 L12 27 M17 21 L22 27" stroke="#fff" stroke-width="2" stroke-linecap="round"/></svg>
      <div class="step-name">Frame</div>
      <p class="step-copy">Change your frame. Posture is an outer reflection of your inner health. Pain, fatigue and many common health conditions result from poor posture. Spinal adjustments twice a week will realign your frame, getting you back into shape and supercharging your body's innate healing power.</p>
    </div>
    <div class="step col-b" style="top:230px">
      <svg class="step-icon" viewBox="0 0 34 34"><circle cx="17" cy="17" r="17" fill="#7cbb2c"/><circle cx="19" cy="9" r="2.8" fill="#fff"/><path d="M18 13 L15 20 L19 23 L18 28 M15 20 L11 26 M17 15 L22 18 M16 15 L12 17" stroke="#fff" stroke-width="2" stroke-linecap="round" fill="none"/></svg>
      <div class="step-name">Flow</div>
      <p class="step-copy">Flow is movement. Commit to walking for half an hour daily to get your body in flow. We've made it simple to track using our Flow App. Then what's your next move? What happens when you complete this programme and truly join Wide Open Sky? Take our Find Your Flow Survey and see if you're ready to join our Unbreakable Community.</p>
    </div>
    <div class="man-photo" role="img" aria-label="Photo of a man meditating cross-legged on a beach"></div>
  </div>

  <div class="page right">
    <div class="woman-photo" role="img" aria-label="Photo of a woman meditating on a pink yoga mat"></div>
    <p class="intro">One step on its own from this programme will make a difference, but follow all five and you really will join Wide Open Sky and become Unbreakable.</p>
    <div class="included">
      <h3>What's included?</h3>
      <ul>
        <li>Focus Questionnaire access</li>
        <li>Formulation Suite Sessions x 3</li>
        <li>Guided Meditation Downloads x 3</li>
        <li>Wide Open Sky Journal</li>
        <li>Adjustment Sessions x 2 per week</li>
        <li>Flow App access</li>
        <li>Find Your Flow Survey</li>
        <li>Invitation to join our Unbreakable Community</li>
      </ul>
    </div>
    <h3 class="after-title">After This Programme You Will:</h3>
    <div class="outcomes">
      <div class="outcome">Experience clear thinking</div>
      <div class="outcome">Master your physical and emotional health</div>
      <div class="outcome">Conquer your limiting beliefs</div>
      <div class="outcome">Improve confidence, self esteem and resilience</div>
      <div class="outcome">Enjoy amazing posture</div>
      <div class="outcome">Become Unbreakable</div>
    </div>
    <h3 class="price-title">How much would <span>all this mean to you?</span></h3>
    <p class="price-note">One amazing programme, two easy options</p>
    <div class="prices">
      <div class="price"><b>£1297</b><i>one off fee</i></div>
      <div class="price"><b>£452</b><i>x3 monthly instalments</i></div>
    </div>
    <div class="family-photo" role="img" aria-label="Photo of a happy family lying together on green grass"></div>
  </div>
</section>

</body>
</html>
```